FRESH WEB DESIGN FOR A HEALTH - SOCIAL NETWORK

We are currently looking for a creative, fresh, vibrant, inspiring design for a new social network focused on health and nutrition for health professionals (namely nutritionists) and end-users.

Design requirements - IMPORTANT: please see attached file 'LumaGrove web site design scope' for the detailed brief.

The web site requires new design templates with inter-changeable banners and in some cases profile images. It's important for the website to communicate LumaGrove's core values and image which includes fun, vitality, freshness, life fulfillment, trust, integrity and loyalty to the two target groups. Imagery must have a consistent/inter-related theme across all communities, topics and resources, which need to be easily applied to the web site.To help engage our audience we are looking for something fresh and unique in the selected imagery/ theme/ design templates.

The chosen design will need to be applied to create a PDF, PowerPoint and business card template.

Please see attached file 'LumaGrove web site design scope' to view the LumaGrove web site, which is currently under development.

Industry/Entity Type

Nutrition

```html
<!DOCTYPE html>
<html lang="en">
<head>
<meta charset="utf-8">
<title>LumaGrove – Improve Your Health</title>
<link rel="stylesheet" href="https://fonts.googleapis.com/css2?family=Exo:wght@200;300;400;500;600;700;800&family=Open+Sans:wght@400;600&display=swap">
<style>
  :root {
    --lime: #b6d136;
    --lime-soft: #cfe172;
    --blue: #4298cf;
    --blue-deep: #1d7fc0;
    --orange: #f07d22;
    --olive: #b5c632;
    --leaf: #56a02b;
    --grey-title: #6b6b6b;
    --text: #9a9a9a;
    --rule: #cfcfcf;
    --band: #f7f7f7;
    --white: #ffffff;
  }
  * { box-sizing: border-box; margin: 0; padding: 0; }
  html, body { width: 971px; height: 1200px; overflow: hidden; }
  body { position: relative; background: var(--white); font-family: "Open Sans", Arial, sans-serif; color: var(--text); }
  .abs { position: absolute; }

  /* header */
  .site-header { position: absolute; left: 0; top: 0; width: 971px; height: 84px; background: var(--lime); border-bottom: 2px solid #c9dd6a; }
  .brand { position: absolute; display: flex; align-items: center; gap: 8px; font-family: "Exo", sans-serif; font-weight: 700; color: var(--white); }
  .brand-dot { border-radius: 50%; background: var(--white); flex: none; }
  .site-header .brand { left: 140px; top: 24px; font-size: 25px; }
  .site-header .brand-dot { width: 30px; height: 30px; }
  .main-nav { position: absolute; top: 37px; left: 0; font-family: "Exo", sans-serif; font-size: 11px; color: var(--white); text-transform: uppercase; letter-spacing: .2px; }
  .main-nav a { position: absolute; color: inherit; text-decoration: none; white-space: nowrap; }
  .main-nav a.is-active { font-weight: 700; }
  .social { position: absolute; width: 24px; height: 24px; border-radius: 50%; }
  .site-header .social { top: 30px; background: var(--lime-soft); }

  /* hero */
  .slider-arrow { position: absolute; top: 235px; width: 42px; height: 42px; border: 1px solid #e2e2e2; border-radius: 50%; }
  .slider-arrow svg { position: absolute; left: 15px; top: 13px; }
  .hero-photo { left: 138px; top: 105px; width: 368px; height: 310px; background: radial-gradient(ellipse at 50% 85%, #e4553a 0%, #7fae3c 30%, rgba(255,255,255,0) 62%), radial-gradient(ellipse at 48% 35%, #b03a78 0%, #d9a184 22%, rgba(255,255,255,0) 48%); }
  .hero-kicker { left: 459px; top: 146px; font-family: "Exo", sans-serif; font-weight: 200; font-size: 55px; color: var(--lime); line-height: 1; letter-spacing: .5px; }
  .hero-title { left: 455px; top: 192px; font-family: "Exo", sans-serif; font-weight: 800; font-size: 109px; color: var(--blue); line-height: 1; letter-spacing: 1px; }
  .btn { position: absolute; background: var(--lime); color: var(--white); font-family: "Exo", sans-serif; display: flex; align-items: center; justify-content: center; text-transform: uppercase; }
  .btn-expert { left: 600px; top: 310px; width: 232px; height: 55px; font-size: 17px; font-weight: 500; }
  .slider-dots { left: 458px; top: 402px; display: flex; gap: 1px; }
  .slider-dots span { width: 10px; height: 10px; border-radius: 50%; border: 1px solid #cfcfcf; }
  .slider-dots span.is-current { border-color: var(--lime); border-width: 2px; }

  /* topics band */
  .topics { position: absolute; left: 0; top: 427px; width: 971px; height: 440px; background: var(--band); }
  .section-title { position: absolute; font-family: "Exo", sans-serif; font-weight: 600; color: var(--lime); white-space: nowrap; }
  .topics .section-title { left: 0; width: 971px; text-align: center; top: 40px; font-size: 31px; }
  .divider { position: absolute; height: 10px; }
  .divider::before, .divider::after { content: ""; position: absolute; top: 4px; height: 1px; background: var(--rule); }
  .divider i { position: absolute; top: 0; width: 10px; height: 10px; border: 1px solid #bdbdbd; border-radius: 50%; }
  .topics .divider { left: 333px; top: 82px; width: 305px; }
  .topics .divider::before { left: 0; width: 135px; }
  .topics .divider::after { right: 0; width: 134px; }
  .topics .divider i { left: 148px; }

  .topic { position: absolute; width: 220px; height: 124px; }
  .topic-photo { position: absolute; left: 0; top: 0; width: 123px; height: 123px; border: 1px solid #e4e4e4; }
  .topic-body { position: absolute; left: 137px; top: 0; }
  .topic-title { font-family: "Exo", sans-serif; font-weight: 600; font-size: 12.5px; line-height: 16px; text-transform: uppercase; }
  .topic-list { list-style: none; margin-top: 3px; font-size: 8.3px; line-height: 12px; color: var(--text); }
  .topic-list li { padding-left: 7px; position: relative; white-space: nowrap; }
  .topic-list li::before { content: ""; position: absolute; left: 0; top: 5px; width: 2px; height: 2px; background: #bdbdbd; }
  .topic-more { margin-top: 4px; font-family: "Exo", sans-serif; font-weight: 700; font-size: 8.5px; display: flex; align-items: center; gap: 2px; }
  .t-olive { color: var(--olive); } .t-orange { color: var(--orange); } .t-leaf { color: var(--leaf); }
  .t-blue { color: var(--blue); } .t-grey { color: var(--grey-title); } .t-deep { color: var(--blue-deep); }

  /* about */
  .about-video { left: 140px; top: 909px; width: 356px; height: 192px; background: linear-gradient(90deg, #e9d7c4 0%, #f1ece6 45%, #e8e8e6 100%); border: 1px solid #e6e6e6; }
  .play-button { left: 297px; top: 983px; width: 42px; height: 42px; border-radius: 50%; border: 4px solid #4a4a4a; background: rgba(255,255,255,.35); }
  .play-button svg { position: absolute; left: 12px; top: 8px; }
  .about .section-title { left: 517px; top: 908px; font-size: 33px; }
  .about .divider { left: 521px; top: 949px; width: 287px; }
  .about .divider::before { left: 0; width: 135px; }
  .about .divider::after { right: 0; width: 135px; }
  .about .divider i { left: 138px; }
  .about-text { left: 518px; top: 970px; width: 316px; font-size: 8.4px; line-height: 12px; color: var(--text); }
  .btn-read { left: 517px; top: 1062px; width: 116px; height: 34px; font-size: 10.5px; font-weight: 500; }

  /* footer */
  .site-footer { position: absolute; left: 0; top: 1142px; width: 971px; height: 58px; background: var(--lime); }
  .site-footer .brand { left: 140px; top: 16px; font-size: 10.5px; gap: 10px; }
  .site-footer .brand-dot { width: 24px; height: 24px; }
  .site-footer .social { top: 16px; background: var(--white); }
</style>
</head>
<body>

<header class="site-header">
  <div class="brand"><span class="brand-dot"></span>LumaGrove</div>
  <nav class="main-nav">
    <a class="is-active" style="left:372px">Home</a>
    <a style="left:419px">About</a>
    <a style="left:471px">Health</a>
    <a style="left:528px">Nutrition</a>
    <a style="left:599px">Features</a>
    <a style="left:669px">Blog</a>
    <a style="left:712px">Contact</a>
  </nav>
  <span class="social" style="left:777px" aria-label="Social link"></span>
  <span class="social" style="left:808px" aria-label="Social link"></span>
</header>

<section class="hero">
  <span class="slider-arrow" style="left:43px">
    <svg width="10" height="14" viewBox="0 0 10 14"><path d="M7 1 1 7l6 6" fill="none" stroke="#c4c4c4" stroke-width="1.5"/></svg>
  </span>
  <span class="slider-arrow" style="left:879px">
    <svg width="10" height="14" viewBox="0 0 10 14"><path d="M3 1l6 6-6 6" fill="none" stroke="#c4c4c4" stroke-width="1.5"/></svg>
  </span>
  <div class="abs hero-photo" role="img" aria-label="Smiling woman leaning over a spread of fresh vegetables: peppers, tomatoes, carrots and greens"></div>
  <div class="abs hero-kicker">IMPROVE YOUR</div>
  <div class="abs hero-title">HEALTH</div>
  <a class="btn btn-expert">Ask an Expert</a>
  <div class="abs slider-dots"><span class="is-current"></span><span></span><span></span><span></span><span></span></div>
</section>

<section class="topics">
  <h2 class="section-title">CORPORATE IMAGERY</h2>
  <div class="divider"><i></i></div>
</section>

<article class="topic" style="left:140px;top:551px">
  <div class="topic-photo" role="img" aria-label="Fresh salad with tomato on a fork" style="background:linear-gradient(135deg,#9ccc4a,#e4503a 55%,#f3d9cf)"></div>
  <div class="topic-body">
    <h3 class="topic-title t-olive">Nutrition</h3>
    <ul class="topic-list"><li>Maintaining Health</li><li>Starting a Healthy</li><li>Health Problem</li><li>Lacking Energy</li><li>Weight Problem</li><li>Pregnancy</li></ul>
    <div class="topic-more t-olive">MORE <svg width="8" height="7" viewBox="0 0 8 7"><path d="M1 1l2.5 2.5L1 6M4.5 1 7 3.5 4.5 6" fill="none" stroke="currentColor" stroke-width="1.3"/></svg></div>
  </div>
</article>

<article class="topic" style="left:379px;top:551px">
  <div class="topic-photo" role="img" aria-label="Woman eating a bowl of salad" style="background:linear-gradient(160deg,#8fd0cf,#c9a48a 50%,#8cc060)"></div>
  <div class="topic-body">
    <h3 class="topic-title t-orange">Health</h3>
    <ul class="topic-list"><li>Maintaining Health</li><li>Starting a Healthy</li><li>Health Problem</li><li>Lacking Energy</li><li>Weight Problem</li><li>Pregnancy</li></ul>
    <div class="topic-more t-orange">MORE <svg width="8" height="7" viewBox="0 0 8 7"><path d="M1 1l2.5 2.5L1 6M4.5 1 7 3.5 4.5 6" fill="none" stroke="currentColor" stroke-width="1.3"/></svg></div>
  </div>
</article>

<article class="topic" style="left:619px;top:548px">
  <div class="topic-photo" role="img" aria-label="Woman jogging along the seaside" style="background:linear-gradient(180deg,#f4f8fb 0%,#d8ecf4 55%,#7fc4dc 70%,#eaeaea 100%)"></div>
  <div class="topic-body" style="top:3px">
    <h3 class="topic-title t-leaf">Wellness</h3>
    <ul class="topic-list"><li>Maintaining Health</li><li>Starting a Healthy</li><li>Health Problem</li><li>Lacking Energy</li><li>Weight Problem</li><li>Pregnancy</li></ul>
    <div class="topic-more t-leaf">MORE <svg width="8" height="7" viewBox="0 0 8 7"><path d="M1 1l2.5 2.5L1 6M4.5 1 7 3.5 4.5 6" fill="none" stroke="currentColor" stroke-width="1.3"/></svg></div>
  </div>
</article>

<article class="topic" style="left:140px;top:696px">
  <div class="topic-photo" role="img" aria-label="Group of four friends in fitness wear" style="background:linear-gradient(180deg,#8fcde6,#d9d0cc 55%,#3a3a44)"></div>
  <div class="topic-body">
    <h3 class="topic-title t-blue">Mind</h3>
    <ul class="topic-list"><li>Maintaining Health</li><li>Starting a Healthy</li><li>Health Problem</li><li>Lacking Energy</li><li>Weight Problem</li><li>Pregnancy</li></ul>
    <div class="topic-more t-blue">MORE <svg width="8" height="7" viewBox="0 0 8 7"><path d="M1 1l2.5 2.5L1 6M4.5 1 7 3.5 4.5 6" fill="none" stroke="currentColor" stroke-width="1.3"/></svg></div>
  </div>
</article>

<article class="topic" style="left:379px;top:696px">
  <div class="topic-photo" role="img" aria-label="Couple running on treadmills in a gym" style="background:linear-gradient(135deg,#d8d8d8,#9a9a9a 50%,#4a4a4a)"></div>
  <div class="topic-body">
    <h3 class="topic-title t-grey">Excercise</h3>
    <ul class="topic-list"><li>Maintaining Health</li><li>Starting a Healthy</li><li>Health Problem</li><li>Lacking Energy</li><li>Weight Problem</li><li>Pregnancy</li></ul>
    <div class="topic-more t-grey">MORE <svg width="8" height="7" viewBox="0 0 8 7"><path d="M1 1l2.5 2.5L1 6M4.5 1 7 3.5 4.5 6" fill="none" stroke="currentColor" stroke-width="1.3"/></svg></div>
  </div>
</article>

<article class="topic" style="left:619px;top:696px">
  <div class="topic-photo" role="img" aria-label="Woman doing push-ups with dumbbells in a gym" style="background:linear-gradient(160deg,#f2f2f2,#b9b9b9 50%,#2e2e2e)"></div>
  <div class="topic-body">
    <h3 class="topic-title t-deep">Energy</h3>
    <ul class="topic-list"><li>Maintaining Health</li><li>Starting a Healthy</li><li>Health Problem</li><li>Lacking Energy</li><li>Weight Problem</li><li>Pregnancy</li></ul>
    <div class="topic-more t-deep">MORE <svg width="8" height="7" viewBox="0 0 8 7"><path d="M1 1l2.5 2.5L1 6M4.5 1 7 3.5 4.5 6" fill="none" stroke="currentColor" stroke-width="1.3"/></svg></div>
  </div>
</article>

<section class="about">
  <div class="abs about-video" role="img" aria-label="Video still of a woman chopping vegetables in a bright kitchen"></div>
  <span class="abs play-button"><svg width="14" height="18" viewBox="0 0 14 18"><path d="M1 1l12 8-12 8z" fill="#4a4a4a"/></svg></span>
  <h2 class="section-title">ABOUT LUMAGROVE</h2>
  <div class="divider"><i></i></div>
  <p class="abs about-text">Lorem ipsum dolor sit amet, consectetuer adipiscing elit, sed diam nonummy nibh euismod tincidunt ut laoreet dolore magna aliquam erat volutpat. Ut wisi enim ad minim veniam, quis nostrud exerci tation ullamcorper suscipit lobortis nisl ut aliquip ex ea commodo consequat. Duis autem vel eum iriure dolor in hendrerit in vulputate velit esse molestie consequat, vel illum dolore eu feugiat nulla facilisis at vero eros et accumsan et iusto odio dignissim qui blandit praesent luptatum zzril delenit augue duis dolore te feugait nulla facilisi.</p>
  <a class="btn btn-read">Read More</a>
</section>

<footer class="site-footer">
  <div class="brand"><span class="brand-dot"></span>© 2014. LUMAGROVE</div>
  <span class="social" style="left:709px" aria-label="Social link"></span>
  <span class="social" style="left:742px" aria-label="Social link"></span>
  <span class="social" style="left:775px" aria-label="Social link"></span>
  <span class="social" style="left:808px" aria-label="Social link"></span>
</footer>

</body>
</html>
```